Industrial design for commercialization of products for cargo

Good morning, we need a website design divided into 4 sections for a newly created company. Torvelix means Industrial Products for Loading and Pumping. We are located in the capital of Mexico and distributed throughout the country. We sell a wide range of equipment and accessories, for handling and lifting of load: hoists, traction devices, trolleys, pulleys, cables, shackles, tensioners, rings, marine chains, among others, as well as pneumatic double diaphragm pumps And centrifugal pumps, used in the pharmaceutical, chemical, food, etc. industries. Our products are manufactured to the highest quality standards, most are manufactured in the United States. Recently, Artmosaic Hub (KALT.MERON) produced our company logo and we would like our website to be combined with it. We want the website to have an industrial design, that the colors combine with the logo and black letters. The images and information that we will use are in our current web page: www.torvelix-demo.com. If you need more information, please let us know. My name is Lidia Quevara and my email is ventastorvelix@mailbox-demo.net. Thank you. PD Please, I want the winner to upload to my server, the coded files html and CSS through FTP (File Transfer Protocol) I know this action means an extra cost, but I m willing to pay. Thanks.
Target Market(s)
Our market is very broad, among our clients are companies in the construction industry, manufacturing, as well as department stores, warehouses, even shops, seaports.
Industry/Entity Type
Commercial
Coding
Coded - Design and coding required
Number of Pages Required
5+ page
Font styles to use
Other font styles liked:
- Hay libertad en cuanto a la tipografía, pueden utilizar la que ustedes consideren conveniente.

Colors
Designer to choose colors to be used in the design.
Requirements
Must have
- The page that we want should be divided into the sections that you consider convenient. SECTION OF HOME INFORMATION.- Our data, biography, mission, vision, values, company address, telephone number, whatsapp, email and location map. PRODUCTS FOR LOADING. PRODUCTS FOR PUMPING. ACCESSORIES FOR LOADING. CONTACT.

Nice to have
- One design you can use as an example is the page of one of our suppliers: www.vultenor.com.mx, we would like our page to be better than that of this provider. We want you to have a better presentation. I would like them to use banners at the top and bottom where phone numbers are placed. I wish there was a space for the videos to run the products. My page must be in the Spanish language please. The choice of colors is at your discretion, however instead of the color orange, I would like them to use the color red.

Should not have
- My project should not seem unprofessional, but to show that we are a serious and important company. Do not look anything like our current page www.torvelix-demo.com We do not want the option to add to the shopping cart or a page with a catalog. Our page is just a means to promote our products. Sales are done by phone.

```html
<!DOCTYPE html>
<html lang="es">
<head>
<meta charset="utf-8">
<title>Torvelix · Productos industriales para carga y bombeo</title>
<link rel="stylesheet" href="https://fonts.googleapis.com/css2?family=Fira+Sans:wght@300;400;500;700&display=swap">
<style>
:root{
  --red:#c8102e;
  --ink:#333333;
  --line:#555555;
  --paper:#ffffff;
  --hero-bg:#f3f4f6;
  --footer:#3b3b3b;
}
*{box-sizing:border-box;margin:0;padding:0}
html,body{width:1066px;height:1200px;overflow:hidden;background:var(--paper)}
body{font-family:"Fira Sans",sans-serif;font-weight:300;color:var(--ink);position:relative}
a{color:inherit;text-decoration:none}

.brand{position:absolute;left:88px;top:18px;display:flex;align-items:center;gap:10px}
.brand-mark{width:46px;height:46px;border:3px solid var(--red)}
.brand-name{font-weight:700;font-size:28px;color:var(--ink);letter-spacing:.5px}
.brand-sub{position:absolute;left:152px;top:53px;font-size:7px;font-weight:500;color:var(--ink);letter-spacing:.2px;text-transform:uppercase}

.phone{position:absolute;right:84px;top:28px;display:flex;align-items:center;gap:6px;color:var(--red);font-weight:500;font-size:15px}

.main-nav{position:absolute;right:84px;top:76px;display:flex;gap:34px;font-size:13.5px;font-weight:400}
.main-nav .active{color:var(--red);font-weight:500}
.caret::after{content:"";display:inline-block;margin-left:3px;border:4px solid transparent;border-top:5px solid currentColor;border-bottom:0;vertical-align:2px}

.hero{position:absolute;left:82px;top:109px;width:900px;height:400px;background:var(--hero-bg);overflow:hidden}
.hero-photo{position:absolute;left:310px;top:0;width:590px;height:400px;background:linear-gradient(120deg,#f4f5f7 0%,#e6e8ec 40%,#8a8e96 70%,#b7bcc4 100%)}
.hero-fade{position:absolute;left:250px;top:0;width:200px;height:400px;background:linear-gradient(90deg,var(--hero-bg),rgba(243,244,246,0))}
.hero h1{position:absolute;left:26px;top:76px;font-weight:400;font-size:24px;color:var(--red);letter-spacing:.3px}
.hero p{position:absolute;left:66px;top:163px;font-size:15px;line-height:27px;color:var(--ink)}
.btn-outline{display:inline-block;border:1px solid var(--red);color:var(--red);font-size:15px;font-weight:400;text-align:center}
.hero .btn-outline{position:absolute;left:368px;top:330px;width:165px;height:40px;line-height:38px;background:rgba(255,255,255,.6)}

.section-title{position:absolute;left:0;width:1066px;text-align:center;font-weight:400;font-size:18px;color:var(--red)}

.card{position:absolute;width:286px;height:263px;border:1px solid var(--line);background:var(--paper)}
.card-head{height:45px;border-bottom:1px solid var(--line);text-align:center;line-height:45px;font-size:15px;font-weight:400}
.card-img{position:absolute;left:67px;top:50px;width:150px;height:150px;border-radius:50%;border:1px solid var(--line);overflow:hidden;display:flex;align-items:center;justify-content:center}
.card-img span{width:100px;height:110px;border-radius:8px}
.card .btn-outline{position:absolute;left:60px;top:209px;width:165px;height:40px;line-height:38px}
.card.featured{border-color:var(--red)}
.card.featured .card-head{color:var(--red);border-color:var(--red)}
.card.featured .card-img{border-color:var(--red)}
.card.featured .btn-outline{background:var(--red);color:#fff}

.slider-arrow{position:absolute;top:962px;width:32px;height:32px}
.partner{position:absolute;top:962px;height:32px;line-height:32px;font-size:20px;font-weight:500;text-align:center}

.site-footer{position:absolute;left:84px;top:1132px;width:899px;height:68px;background:var(--footer);color:#fff;display:flex;align-items:center;padding:0 14px 0 24px}
.site-footer small{font-size:11px;font-weight:400;width:190px}
.footer-nav{display:flex;gap:37px;font-size:13.5px;font-weight:400;margin-left:auto}
</style>
</head>
<body>

<header>
  <a class="brand" href="#"><span class="brand-mark"></span><span class="brand-name">TORVELIX</span></a>
  <div class="brand-sub">Productos industriales para carga y bombeo</div>
  <div class="phone">
    <svg width="14" height="14" viewBox="0 0 24 24" fill="currentColor" aria-hidden="true"><path d="M6.6 10.8a15.1 15.1 0 0 0 6.6 6.6l2.2-2.2c.3-.3.7-.4 1-.2 1.1.4 2.3.6 3.6.6.6 0 1 .4 1 1V20c0 .6-.4 1-1 1A17 17 0 0 1 3 4c0-.6.4-1 1-1h3.5c.6 0 1 .4 1 1 0 1.2.2 2.4.6 3.6.1.3 0 .7-.2 1z"/></svg>
    (01 55) 4812 3096
  </div>
  <nav class="main-nav">
    <a class="active" href="#">INICIO</a>
    <a class="caret" href="#">PRODUCTOS PARA CARGA</a>
    <a class="caret" href="#">PRODUCTOS PARA BOMBEO</a>
    <a class="caret" href="#">ACCESORIOS</a>
    <a href="#">CONTACTO</a>
  </nav>
</header>

<section class="hero">
  <div class="hero-photo" role="img" aria-label="Ejecutivo firmando documentos en un escritorio de oficina"></div>
  <div class="hero-fade"></div>
  <h1>QUIÉNES SOMOS EN TORVELIX...</h1>
  <p>Somos un equipo competente y eficaz.<br>Le ofrecemos una amplia gama de productos<br>de alta calidad a unos precios muy competitivos.<br>Le respaldamos con un equipo que se caracteriza<br>por su trato cordial y espíritu de servicio.</p>
  <a class="btn-outline" href="#">Más información</a>
</section>

<h2 class="section-title" style="top:536px">PRODUCTOS</h2>

<article class="card" style="left:84px;top:583px">
  <div class="card-head">PRODUCTOS PARA CARGA</div>
  <div class="card-img"><span role="img" aria-label="Polipasto de palanca con cadena" style="background:linear-gradient(160deg,#e0573a,#b9bcc2)"></span></div>
  <a class="btn-outline" href="#">Más información aquí</a>
</article>

<article class="card featured" style="left:390px;top:575px">
  <div class="card-head">PRODUCTOS PARA BOMBEO</div>
  <div class="card-img"><span role="img" aria-label="Bombas neumáticas de doble diafragma" style="width:120px;height:100px;background:linear-gradient(135deg,#e8632c,#b9461d)"></span></div>
  <a class="btn-outline" href="#" style="top:210px">Más información aquí</a>
</article>

<article class="card" style="left:698px;top:583px">
  <div class="card-head">ACCESORIOS</div>
  <div class="card-img"><span role="img" aria-label="Gancho de elevación rojo" style="width:70px;background:linear-gradient(160deg,#d21f3a,#8f1024)"></span></div>
  <a class="btn-outline" href="#">Más información aquí</a>
</article>

<h2 class="section-title" style="top:879px">DISTRIBUIDORES</h2>

<svg class="slider-arrow" style="left:92px" viewBox="0 0 32 32" aria-label="Anterior"><circle cx="16" cy="16" r="15" fill="none" stroke="#333" stroke-width="1.5"/><path d="M19 10v12l-8-6z" fill="#333"/></svg>
<div class="partner" style="left:136px;width:190px;color:var(--red)">Dornholt Group</div>
<div class="partner" style="left:433px;width:200px;color:#6d6e71">Marvane Lifting</div>
<div class="partner" style="left:770px;width:140px;color:#1f5fae">Keltrana</div>
<svg class="slider-arrow" style="left:946px" viewBox="0 0 32 32" aria-label="Siguiente"><circle cx="16" cy="16" r="15" fill="none" stroke="#333" stroke-width="1.5"/><path d="M13 10v12l8-6z" fill="#333"/></svg>

<footer class="site-footer">
  <small>Copyright © 2017 Torvelix</small>
  <nav class="footer-nav">
    <a href="#">INICIO</a>
    <a class="caret" href="#">PRODUCTOS PARA CARGA</a>
    <a class="caret" href="#">PRODUCTOS PARA BOMBEO</a>
    <a class="caret" href="#">ACCESORIOS</a>
    <a href="#">CONTACTO</a>
  </nav>
</footer>

</body>
</html>
```